Delvin & Associates - London New Letting and Property Management Company *

Delvin & Associates LTD is a new company based in London, and works with brand new residential property in the city centre.

We are aiming to have 1000 new properties a year.

We are looking for something modern and minimalistic :
Logo ,Monogram, Paper Head and Business Card.

Target Market(s)

Internation landlords

Industry/Entity Type

Real Estate

Logo Text

Delvin & Associates

Colors

Designer to choose colors to be used in the design.

Requirements
Nice to have
• A particular monogram with "DA"
Should not have
• Little House over the logo

```html
<!DOCTYPE html>
<html lang="en">
<head>
<meta charset="utf-8">
<title>Delvin & Associates — Business Card</title>
<link rel="stylesheet" href="https://fonts.googleapis.com/css2?family=Exo+2:wght@400;500;700&display=swap">
<style>
  :root {
    --canvas: #e9e9e9;
    --ink: #2a2a2b;
    --paper: #f4f4f4;
    --white: #ffffff;
    --muted: #555555;
  }
  * { margin: 0; padding: 0; box-sizing: border-box; }
  html, body { width: 1200px; height: 900px; overflow: hidden; }
  body {
    background: var(--canvas);
    font-family: "Exo 2", "Segoe UI", sans-serif;
    display: flex;
    flex-direction: column;
    align-items: center;
    justify-content: center;
    gap: 60px;
  }
  .card {
    width: 600px;
    height: 340px;
    position: relative;
    overflow: hidden;
    box-shadow: 0 6px 18px rgba(0,0,0,0.12);
  }

  /* Front */
  .card-front { background: var(--ink); }
  .card-front .monogram {
    position: absolute;
    top: 0; left: 0; right: 0; bottom: 72px;
    display: flex; align-items: center; justify-content: center;
    color: var(--white);
    font-size: 68px;
    font-weight: 700;
    letter-spacing: 2px;
  }
  .card-front .tagline-band {
    position: absolute;
    left: 0; right: 0; bottom: 0;
    height: 72px;
    background: var(--white);
    display: flex; align-items: center; justify-content: center;
  }
  .tagline {
    color: var(--ink);
    font-size: 15px;
    font-weight: 500;
    letter-spacing: 1.5px;
    text-transform: uppercase;
  }

  /* Back */
  .card-back { display: flex; }
  .brand-panel {
    width: 48%;
    background: var(--ink);
    color: var(--white);
    display: flex; flex-direction: column;
    align-items: center; justify-content: center;
    gap: 18px;
  }
  .brand-panel .monogram { font-size: 56px; font-weight: 700; letter-spacing: 2px; }
  .brand-panel .company {
    font-size: 15px;
    font-weight: 400;
    letter-spacing: 2px;
    text-transform: uppercase;
  }
  .contact-panel {
    flex: 1;
    background: var(--paper);
    color: var(--ink);
    padding: 48px 34px;
    display: flex; flex-direction: column; justify-content: center;
  }
  .person-name { font-size: 20px; font-weight: 700; }
  .person-role { font-size: 13px; color: var(--muted); margin-top: 2px; margin-bottom: 20px; }
  .contact-list { list-style: none; display: flex; flex-direction: column; gap: 8px; }
  .contact-list li { display: flex; align-items: center; gap: 10px; font-size: 14px; }
  .contact-list li.address { font-weight: 500; margin-bottom: 12px; }
  .icon {
    width: 16px; height: 16px;
    background: var(--ink);
    display: inline-flex; align-items: center; justify-content: center;
    flex-shrink: 0;
  }
  .icon svg { width: 10px; height: 10px; }
</style>
</head>
<body>

  <section class="card card-front" aria-label="Business card front">
    <div class="monogram">DA</div>
    <div class="tagline-band">
      <p class="tagline">Professional Real Estate</p>
    </div>
  </section>

  <section class="card card-back" aria-label="Business card back">
    <div class="brand-panel">
      <div class="monogram">DA</div>
      <p class="company">Delvin &amp; Associates LTD</p>
    </div>
    <div class="contact-panel">
      <p class="person-name">Daniel Aston</p>
      <p class="person-role">Director</p>
      <ul class="contact-list">
        <li class="address">
          <span class="icon"><svg viewBox="0 0 10 10"><path d="M5 0.5a3 3 0 0 0-3 3c0 2.3 3 6 3 6s3-3.7 3-6a3 3 0 0 0-3-3z" fill="#fff"/><circle cx="5" cy="3.5" r="1.1" fill="#2a2a2b"/></svg></span>
          Your Address Here
        </li>
        <li>
          <span class="icon"><svg viewBox="0 0 10 10"><path d="M2 0.8l1.6 0 0.8 2.2-1 0.8a5.5 5.5 0 0 0 2.8 2.8l0.8-1 2.2 0.8 0 1.6c0 0.5-0.4 0.9-0.9 0.9A8 8 0 0 1 1.1 1.7c0-0.5 0.4-0.9 0.9-0.9z" fill="#fff"/></svg></span>
          111. 222. 333. 444
        </li>
        <li>
          <span class="icon"><svg viewBox="0 0 10 10"><rect x="2.5" y="0.5" width="5" height="9" rx="1" fill="#fff"/><rect x="3.5" y="1.8" width="3" height="5.6" fill="#2a2a2b"/></svg></span>
          555. 666. 777. 888
        </li>
        <li>
          <span class="icon"><svg viewBox="0 0 10 10"><rect x="0.5" y="2" width="9" height="6" fill="#fff"/><path d="M0.5 2l4.5 3.4 4.5-3.4" stroke="#2a2a2b" stroke-width="0.9" fill="none"/></svg></span>
          email@website.com
        </li>
        <li>
          <span class="icon"><svg viewBox="0 0 10 10"><circle cx="5" cy="5" r="4.2" fill="none" stroke="#fff" stroke-width="1"/><ellipse cx="5" cy="5" rx="1.8" ry="4.2" fill="none" stroke="#fff" stroke-width="0.8"/><line x1="0.8" y1="5" x2="9.2" y2="5" stroke="#fff" stroke-width="0.8"/></svg></span>
          www.website.com
        </li>
      </ul>
    </div>
  </section>

</body>
</html>
```